Design AND code an HTML landing page

A landing page for campaigns and webinars respondents for project www.brevamor-homes.example. We expect the design to be coded. We will provide the copy and content. It will be a simple landing page for a new development project, to capture details of any potential clients showing interest, including any leads generated via webinars.

Broad instructions are as follows:
- It should not have a header or footer. Minimum escape links as possible.
- Create a lead generator box to get e-mails / relevant info of people interested.
- If possible, add a virtual tour (link to host server provided) at the top of the page.
- Content will be provided
- An option to include a link to a ClipVerra video

Target Market(s)

Pre/retiree and retirees

Industry/Entity Type

Real estate development, retirement, relocation, travel and tourism

Coding

Coded - Design and coding required

Font styles to use
Other font styles liked:
• Preferably same as existing site

Colors
FFF300
FFF600
FEFA6F
FFFEC7
FFFEE8

Requirements
Must have
• Simple yet appealing look and feel, within the motif of the project, simple list of questions
Should not have
• Emojis, unrelated graphics, excessive graphics that are not linked to project

```html
<!DOCTYPE html>
<html lang="en">
<head>
<meta charset="utf-8">
<title>Brevamor living – Real Estate Leads</title>
<link href="https://fonts.googleapis.com/css2?family=Playfair+Display:wght@400;700&family=Poppins:wght@300;400;500;600&display=swap" rel="stylesheet">
<style>
:root{
  --yellow:#fff300;
  --yellow-soft:#fffbb0;
  --yellow-dots:#fff77a;
  --ink:#111111;
  --text:#333333;
  --white:#ffffff;
  --footer:#808080;
  --dots:#f6f6f9;
  --icon-bg:#f2f2f2;
}
*{box-sizing:border-box;margin:0;padding:0}
html,body{width:696px;height:1200px;overflow:hidden;background:var(--white)}
body{position:relative;font-family:'Poppins',sans-serif;color:var(--text)}
.abs{position:absolute}
.serif{font-family:'Playfair Display',serif}

.hero-photo{left:0;top:0;width:696px;height:346px}
.brand{left:83px;top:18px;font-size:17px;font-weight:500;color:var(--ink);letter-spacing:.2px}
.tour-btn{left:530px;top:17px;width:81px;height:23px;background:var(--white);border-radius:3px;display:flex;align-items:center;font-size:7px;color:var(--ink);overflow:hidden}
.tour-btn .tour-icon{width:26px;height:23px;background:var(--yellow);display:flex;align-items:center;justify-content:center;margin-right:7px}

.hero-title{left:83px;top:104px;font-size:21px;font-weight:400;color:var(--ink)}
.hero-title mark{background:var(--yellow);color:var(--ink);padding:0 2px;font-weight:700}
.hero-copy{left:83px;top:137px;width:260px;font-size:6.6px;line-height:11px;color:#222}
.hero-note{left:83px;top:166px;font-size:8.4px;font-weight:500;color:var(--ink)}
.lead-form{width:215px;height:34px;background:var(--white);border-radius:3px;box-shadow:0 2px 8px rgba(0,0,0,.12);display:flex;align-items:center;justify-content:space-between;padding:0 5px 0 13px}
.lead-form input{border:0;outline:0;font-family:'Poppins',sans-serif;font-size:7.3px;width:120px;color:var(--text);background:transparent}
.lead-form input::placeholder{color:#888}
.lead-form button{background:var(--ink);color:var(--yellow);border:0;border-radius:3px;font-family:'Poppins',sans-serif;font-weight:600;font-size:7.4px;height:25px;width:72px}
.hero-form{left:83px;top:193px}

.feature{top:359px;width:140px;text-align:center}
.feature .icon{width:50px;height:50px;border-radius:50%;background:var(--icon-bg);margin:0 auto 6px;display:flex;align-items:center;justify-content:center}
.feature h3{font-family:'Playfair Display',serif;font-weight:700;font-size:8.6px;color:var(--ink);margin-bottom:2px}
.feature p{font-size:6.6px;line-height:11px;color:#444}

.dots{background:var(--dots)}
.video-band{left:0;top:475px;width:696px;height:275px;background:var(--yellow)}
.video-title{left:0;top:506px;width:696px;text-align:center;font-size:19.5px;font-weight:700;color:var(--ink)}
.video-copy{left:0;top:545px;width:696px;text-align:center;font-size:8.4px;line-height:17px;color:#222}
.video-copy strong{font-weight:600;color:var(--ink)}
.video{left:83px;top:591px;width:529px;height:334px;background:linear-gradient(180deg,#9a9a9a 0%,#c9c9c9 38%,#6f6f6f 62%,#2c2c2c 100%)}
.play{left:244px;top:146px;width:40px;height:40px;border-radius:50%;background:rgba(0,0,0,.55);border:1.5px solid rgba(255,255,255,.85);display:flex;align-items:center;justify-content:center}
.controls{left:6px;bottom:6px;width:517px;height:16px;color:#fff;font-size:5px;display:flex;align-items:center;gap:8px}
.progress{left:6px;bottom:17px;width:517px;height:1.5px;background:rgba(255,255,255,.35)}
.progress span{display:block;width:67px;height:100%;background:var(--yellow)}

.talk-sun{left:159px;top:1042px;width:376px;height:376px;border-radius:50%;background:var(--yellow-soft)}
.talk-title{left:0;top:962px;width:696px;text-align:center;font-size:19.5px;font-weight:700;color:var(--ink)}
.talk-copy{left:0;top:997px;width:696px;text-align:center;font-size:8.4px;line-height:17px;color:#222}
.talk-form{left:240px;top:1051px}
.social{top:1116px;width:20px;height:20px;border:1.3px solid var(--ink);border-radius:50%;display:flex;align-items:center;justify-content:center;font-size:4.2px;font-weight:600;color:var(--ink)}
.footer{left:0;top:1162px;width:696px;height:38px;background:var(--footer);display:flex;align-items:center;justify-content:center;font-size:6px;color:#eeeeee}
</style>
</head>
<body>

<svg class="abs hero-photo" viewBox="0 0 696 346" role="img" aria-label="Photo of a businessman in a suit with arms crossed before a hazy city skyline">
  <defs>
    <linearGradient id="heroTone" x1="0" y1="0" x2="1" y2="0">
      <stop offset="0" stop-color="#d9dcdc"/>
      <stop offset=".5" stop-color="#c4c7c7"/>
      <stop offset=".62" stop-color="#4a4d4f"/>
      <stop offset="1" stop-color="#2d3032"/>
    </linearGradient>
  </defs>
  <path d="M0,0 H696 V256 C670,248 650,240 630,244 C590,252 560,318 470,318 C400,318 360,298 300,300 C240,302 190,346 140,345 C80,344 30,292 0,252 Z" fill="url(#heroTone)"/>
</svg>

<div class="abs brand">Brevamor living</div>

<a class="abs tour-btn">
  <span class="tour-icon"><svg width="12" height="12" viewBox="0 0 12 12" fill="none" stroke="#111" stroke-width="1"><circle cx="6" cy="3" r="1.6"/><path d="M6 5v4M3 8.5c-1.5.4-1.5 1.8 3 1.8s4.5-1.4 3-1.8"/></svg></span>
  Virtual Tour
</a>

<h1 class="abs hero-title serif">Get More <mark>Real Estate</mark> Leads</h1>
<p class="abs hero-copy">Get a guaranteed number of home buyer &amp; seller leads in your local market every month that are exclusive—not shared with other agents.</p>
<p class="abs hero-note">Lead inventory is limited, so check availability today!</p>

<form class="abs lead-form hero-form"><input type="email" placeholder="Enter your Email Address"><button type="button">Subscribe Now!</button></form>

<svg class="abs" style="left:300px;top:146px" width="40" height="70" viewBox="0 0 40 70" fill="none" stroke="#111" stroke-width="1.2">
  <path d="M35 2 C40 30 25 55 6 63"/><path d="M12 56 L5 63 L14 65"/>
</svg>

<div class="abs dots" style="left:17px;top:419px;width:53px;height:56px" role="img" aria-label="Dot grid decoration"></div>

<div class="abs feature" style="left:60px">
  <div class="icon"><svg width="26" height="26" viewBox="0 0 26 26" fill="none" stroke="#111" stroke-width="1"><path d="M13 3l2.2 4.6 5 .6-3.7 3.4 1 5-4.5-2.5-4.5 2.5 1-5L5.8 8.2l5-.6z" fill="#fff300"/><path d="M5 22h16"/></svg></div>
  <h3>Exclusive to You</h3><p>We'll never send your leads<br>to your competitors</p>
</div>
<div class="abs feature" style="left:191px">
  <div class="icon"><svg width="26" height="26" viewBox="0 0 26 26" fill="none" stroke="#111" stroke-width="1.2"><circle cx="13" cy="13" r="11"/><circle cx="13" cy="13" r="8" fill="#fff300"/><path d="M9 13l3 3 5-6"/></svg></div>
  <h3>Guaranteed Quantity</h3><p>Get more than just market share—pay<br>for 30 leads , get 30 leads a month</p>
</div>
<div class="abs feature" style="left:337px">
  <div class="icon"><svg width="26" height="26" viewBox="0 0 26 26" fill="none" stroke="#111" stroke-width="1.2"><circle cx="12" cy="14" r="10"/><circle cx="12" cy="14" r="6"/><circle cx="12" cy="14" r="2" fill="#fff300"/><path d="M12 14l10-10M19 3l3 1 1 3"/></svg></div>
  <h3>Target Specific Areas</h3><p>Own your local market—get leads<br>where you want them</p>
</div>
<div class="abs feature" style="left:484px">
  <div class="icon"><svg width="26" height="26" viewBox="0 0 26 26" fill="none" stroke="#111" stroke-width="1.1"><rect x="12" y="10" width="11" height="8" fill="#fff300"/><path d="M3 21h20"/></svg></div>
  <h3>Experts Work for You</h3><p>Save time &amp; effort—leads are generated<br>for you by digital advertising experts</p>
</div>

<div class="abs video-band"></div>
<div class="abs" style="left:17px;top:480px;width:53px;height:53px;background:var(--yellow-dots)" role="img" aria-label="Dot grid decoration"></div>
<h2 class="abs video-title serif">Explore Our Introduction Video</h2>
<p class="abs video-copy">This should be used to tell a story abour our product or service.<br><strong>How can you benefit them?</strong></p>
<div class="abs" style="left:633px;top:693px;width:53px;height:113px;background:linear-gradient(180deg,var(--yellow-dots) 0 57px,var(--dots) 57px)" role="img" aria-label="Dot grid decoration"></div>

<div class="abs video" role="img" aria-label="ClipVerra video still of snowy volcanic hills under cloud">
  <div class="abs play"><svg width="14" height="14" viewBox="0 0 14 14"><path d="M4 2l9 5-9 5z" fill="#fff"/></svg></div>
  <div class="abs progress"><span></span></div>
  <div class="abs controls">
    <svg width="8" height="8" viewBox="0 0 8 8"><path d="M1 0l7 4-7 4z" fill="#fff"/></svg>
    <svg width="9" height="8" viewBox="0 0 9 8"><path d="M0 0l6 4-6 4z M7 0h1.5v8H7z" fill="#fff"/></svg>
    <svg width="8" height="8" viewBox="0 0 8 8"><path d="M0 2.5h2l3-2.5v8l-3-2.5H0z" fill="#fff"/></svg>
    <span>0:24 / 3:28</span>
  </div>
</div>

<div class="abs talk-sun"></div>
<svg class="abs" style="left:180px;top:1010px" width="380" height="130" viewBox="0 0 380 130" fill="none" stroke="#999" stroke-width=".7" stroke-dasharray="3 3">
  <path d="M4 128 C10 40 80 20 150 30"/><path d="M275 62 C310 58 330 45 345 30"/>
</svg>
<div class="abs dots" style="left:628px;top:957px;width:53px;height:53px" role="img" aria-label="Dot grid decoration"></div>
<div class="abs dots" style="left:31px;top:1086px;width:53px;height:53px" role="img" aria-label="Dot grid decoration"></div>

<h2 class="abs talk-title serif">Interested In Working With Us Let’s Talk Now</h2>
<p class="abs talk-copy">This should used to tell a story and let your users know a little more about your<br>product or service. How can you benefit them?</p>
<form class="abs lead-form talk-form"><input type="email" placeholder="Enter your Email Address"><button type="button">Subscribe Now!</button></form>

<a class="abs social" style="left:289px">Orbly</a>
<a class="abs social" style="left:321px">Fenno</a>
<a class="abs social" style="left:354px">Lintra</a>
<a class="abs social" style="left:386px">Chirpa</a>

<div class="abs footer">© Brevamor Homes LDA 2021. All Rights Reserved</div>

</body>
</html>
```